Brisa Pastry Mill Business card

We are empanada whole-sellers and I want a business card design with a picture of an empanada on it that also mentions first trial order FREE. our contact number 555-214-7093 our website www.brisapastry.example and business email Tobin@brisapastry.example

If you want any of our artwork please feel free to email me at the address above.

```html
<!DOCTYPE html>
<html lang="en">
<head>
<meta charset="utf-8">
<title>Brisa Pastry Mill – Business Card</title>
<link rel="stylesheet" href="https://fonts.googleapis.com/css2?family=Courier+Prime:wght@400;700&family=Stardos+Stencil:wght@700&family=Alfa+Slab+One&display=swap">
<style>
  :root {
    --page: #d9d9d9;
    --card-white: #ffffff;
    --card-edge: #111111;
    --ink: #111111;
    --sun: #f2c230;
    --sun-light: #ffd95a;
    --sun-deep: #e3a51c;
  }
  html, body {
    margin: 0;
    width: 1200px;
    height: 875px;
    overflow: hidden;
    background: var(--page);
  }
  .canvas {
    position: relative;
    width: 1200px;
    height: 875px;
  }
  .card {
    position: absolute;
    left: 250px;
    width: 700px;
    height: 400px;
    border-radius: 26px;
    overflow: hidden;
    box-sizing: border-box;
  }
  .card--front {
    top: 25px;
    background: var(--card-white);
    border: 10px solid var(--card-edge);
  }
  .card--back {
    top: 450px;
  }

  /* Front: offer block */
  .empanada-art {
    position: absolute;
    left: 18px;
    top: 40px;
    width: 330px;
    height: 290px;
  }
  .offer {
    position: absolute;
    left: 26px;
    top: 96px;
    width: 310px;
    text-align: center;
    color: var(--ink);
  }
  .offer__lead,
  .offer__tail {
    font-family: "Alfa Slab One", serif;
    font-size: 18px;
    letter-spacing: 0.5px;
    line-height: 1;
    white-space: nowrap;
  }
  .offer__headline {
    font-family: "Stardos Stencil", "Courier Prime", monospace;
    font-weight: 700;
    font-size: 100px;
    line-height: 0.95;
    margin: 4px 0 6px;
  }

  /* Front: identity + contact */
  .brand-name {
    position: absolute;
    left: 370px;
    right: 22px;
    top: 88px;
    margin: 0;
    font-family: "Courier Prime", monospace;
    font-weight: 700;
    font-size: 26px;
    line-height: 1;
    text-align: right;
    white-space: nowrap;
    color: var(--ink);
  }
  .contact {
    position: absolute;
    left: 370px;
    right: 22px;
    top: 170px;
    margin: 0;
    padding: 0;
    list-style: none;
    font-family: "Courier Prime", monospace;
    font-size: 17px;
    line-height: 40px;
    text-align: right;
    white-space: nowrap;
    color: var(--ink);
  }

  /* Back */
  .back-pattern {
    position: absolute;
    inset: 0;
    background: linear-gradient(135deg, var(--sun-light), var(--sun) 55%, var(--sun-deep));
  }
  .back-name {
    position: absolute;
    inset: 0;
    display: flex;
    align-items: center;
    justify-content: center;
    margin: 0;
    font-family: "Courier Prime", monospace;
    font-weight: 700;
    font-size: 58px;
    color: var(--ink);
  }
</style>
</head>
<body>
<main class="canvas">

  <section class="card card--front" aria-label="Business card front">
    <svg class="empanada-art" viewBox="0 0 360 290" preserveAspectRatio="none" role="img" aria-label="Illustration of a golden baked empanada">
      <defs>
        <linearGradient id="pastry-tone" x1="0" y1="0" x2="1" y2="1">
          <stop offset="0" stop-color="#ffe08a"/>
          <stop offset="1" stop-color="#f0a92a"/>
        </linearGradient>
      </defs>
      <path d="M20 30 C140 10 300 60 345 230 C300 280 180 285 90 250 C30 220 5 130 20 30 Z" fill="url(#pastry-tone)"/>
    </svg>

    <div class="offer">
      <div class="offer__lead">FIRST TRIAL ORDER</div>
      <div class="offer__headline">FREE</div>
      <div class="offer__tail">WHOLESALE EMPANADAS</div>
    </div>

    <h1 class="brand-name">Brisa Pastry Mill</h1>

    <ul class="contact">
      <li>ph:(555) 214-7093</li>
      <li>e:Tobin@brisapastry.example</li>
      <li>www.brisapastry.example</li>
      <li>www.brisapastry.example</li>
    </ul>
  </section>

  <section class="card card--back" aria-label="Business card back">
    <div class="back-pattern" role="img" aria-label="Yellow background with black and white daisy flower pattern"></div>
    <p class="back-name">Brisa Pastry Mill</p>
  </section>

</main>
</body>
</html>
```